Modern, pro female massage business needs business card design

We are a boutique, pro women's sports and remedial massage studio based in Singapore - we have a logo already (see attached image) and need to design a business card that reflects an elegant, modern and feminine feel using this logo.

We are focussed on a very local market and need to give a professional yet warm feeling.

Details for the card include (layout of your choice):

Tamsin Vale
Call, SMS or WhatsApp: 9183 6027
Email: bluefennel@mailbox-example.com
Address: The Harbourview on Talbot
72 Talbot Road, Westmere, Singapore

To incorporate the QRAB logo (www.qrabglobal.co.uk) would be appreciated - see attached file.

Industry/Entity Type

Massage

Requirements
Nice to have
• We like the idea of using an embossed style card. Solid colour on the reverse - embossed on the front; four colour printing is okay.
Should not have
• It should not be uber 'girly girl' if that makes any sense. The logo is already colourful

```html
<!DOCTYPE html>
<html lang="en">
<head>
<meta charset="utf-8">
<title>bluefennel – Business Card</title>
<link rel="stylesheet" href="https://fonts.googleapis.com/css2?family=Questrial&display=swap">
<style>
  :root {
    --backdrop: #f1f1f1;
    --card-white: #ffffff;
    --card-magenta: #c5126a;
    --magenta-deep: #a80d58;
    --logo-pink: #c2186b;
    --tagline-grey: #5a5a5a;
    --floral-grey: #e4e4e4;
    --floral-pale: #f4d9e6;
    --badge-blue: #2a5f9e;
    --text-on-magenta: #ffffff;
  }
  * { margin: 0; padding: 0; box-sizing: border-box; }
  html, body {
    width: 1200px;
    height: 644px;
    overflow: hidden;
    background: var(--backdrop);
    font-family: "Questrial", "Century Gothic", sans-serif;
  }
  .sheet {
    position: relative;
    width: 1200px;
    height: 644px;
    display: flex;
    align-items: center;
    justify-content: center;
    gap: 60px;
  }
  .card {
    position: relative;
    width: 500px;
    height: 286px;
    border-radius: 22px;
    overflow: hidden;
    box-shadow: 0 10px 28px rgba(0,0,0,0.12);
  }

  /* Front */
  .card--front { background: var(--card-white); }
  .front-floral {
    position: absolute;
    left: 0; bottom: 0;
    width: 230px; height: 200px;
    background: radial-gradient(ellipse at 20% 85%, var(--floral-grey) 0%, rgba(228,228,228,0.6) 45%, rgba(255,255,255,0) 75%);
  }
  .front-logo {
    position: absolute;
    left: 150px; top: 108px;
  }
  .wordmark {
    display: block;
    font-size: 46px;
    line-height: 1;
    letter-spacing: -0.5px;
    color: var(--logo-pink);
  }
  .tagline {
    display: block;
    margin-top: 4px;
    font-size: 14px;
    color: var(--tagline-grey);
    letter-spacing: 0.2px;
  }
  .partner-badge {
    position: absolute;
    right: 24px; top: 22px;
    width: 36px; height: 36px;
    border-radius: 50%;
    background: var(--badge-blue);
  }

  /* Back */
  .card--back { background: var(--card-magenta); }
  .back-floral {
    position: absolute;
    right: 0; top: 0;
    width: 260px; height: 240px;
    background: radial-gradient(ellipse at 85% 15%, var(--floral-pale) 0%, rgba(244,217,230,0.55) 40%, rgba(197,18,106,0) 75%);
  }
  .back-content {
    position: absolute;
    left: 34px; top: 96px;
    color: var(--text-on-magenta);
  }
  .back-content .wordmark {
    font-size: 30px;
    color: var(--text-on-magenta);
  }
  .back-content .tagline {
    font-size: 10px;
    margin-top: 2px;
    color: var(--text-on-magenta);
  }
  .holder-name {
    margin-top: 20px;
    font-size: 14px;
    font-weight: 400;
    letter-spacing: 0.3px;
  }
  .contact-list {
    list-style: none;
    margin-top: 10px;
    font-size: 10.5px;
    line-height: 1.6;
  }
</style>
</head>
<body>
  <main class="sheet">
    <section class="card card--front" aria-label="Card front">
      <div class="front-floral" role="img" aria-label="Soft grey embossed floral pattern"></div>
      <div class="front-logo">
        <span class="wordmark">bluefennel</span>
        <span class="tagline">Remedial and sports massage</span>
      </div>
      <div class="partner-badge" role="img" aria-label="Accreditation badge"></div>
    </section>

    <section class="card card--back" aria-label="Card back">
      <div class="back-floral" role="img" aria-label="Pale pink floral spray decoration"></div>
      <div class="back-content">
        <span class="wordmark">bluefennel</span>
        <span class="tagline">Remedial and sports massage</span>
        <h1 class="holder-name">Tamsin Vale</h1>
        <ul class="contact-list">
          <li>Call, SMS or WhatsApp: 9183 6027</li>
          <li>Email: bluefennel@mailbox-example.com</li>
          <li>Address: The Harbourview on Talbot</li>
          <li>72 Talbot Road, Westmere, Singapore</li>
        </ul>
      </div>
    </section>
  </main>
</body>
</html>
```